Specialty Chemical Product Line Card Revamp

I need a new digital brochure for our product catalog of various chemicals. This will be sent to my customers as a digital file or printed on flat paper (not a folded brochure). I have included the OLD brochure (Tobin Chemical Line Card document) and the new categories that I want used instead (Line Card Categories document). I also included our logo and other photos. I would like the new brochure to be more modern and attention-grabbing

Target Market(s)

Product Manufacturers

Industry/Entity Type

Chemical Product

Font styles to use
Serif
Sans Serif

Requirements
Must have
• Product Category Headers. Company Logo
Nice to have
• Incorporate the attached photos. Use similar colors as the logo. Fit on 2 pages
Should not have
• Cannot be more than 3 pages.

```html
<!DOCTYPE html>
<html lang="en">
<head>
<meta charset="utf-8">
<title>Tobin Chemical – Chemical Product Line Card</title>
<link href="https://fonts.googleapis.com/css2?family=Oswald:wght@500;700&family=Roboto+Condensed:wght@400;700&display=swap" rel="stylesheet">
<style>
  :root {
    --bg: #ffffff;
    --purple: #3b2468;
    --purple-deep: #24143f;
    --green: #8dc63f;
    --green-light: #c4e19a;
    --ink: #2a2a2a;
    --grey: #e9e9ec;
    --grey-mid: #c9c9cf;
  }
  * { box-sizing: border-box; margin: 0; padding: 0; }
  html, body { width: 800px; height: 1200px; overflow: hidden; background: var(--bg); }
  .canvas {
    width: 800px; height: 1200px; display: flex; justify-content: center;
    align-items: center; gap: 14px;
  }
  .page {
    position: relative; width: 385px; height: 500px; background: #fff;
    box-shadow: 0 1px 6px rgba(0,0,0,.18); overflow: hidden;
    font-family: "Roboto Condensed", Arial, sans-serif; color: var(--ink);
  }
  .brand {
    height: 34px; display: flex; align-items: center; justify-content: center; gap: 5px;
  }
  .brand-dot { width: 7px; height: 7px; border-radius: 50%; background: var(--green); }
  .brand-name {
    font-family: "Oswald", Arial, sans-serif; font-weight: 500; font-size: 15px;
    color: var(--purple); letter-spacing: .3px;
  }
  .title-band {
    height: 30px; background: linear-gradient(90deg, var(--purple-deep), var(--purple) 50%, var(--purple-deep));
    border-bottom: 3px solid var(--green);
    display: flex; align-items: center; justify-content: center;
    font-family: "Oswald", Arial, sans-serif; font-weight: 700; font-size: 17px;
    color: #fff; letter-spacing: 1px;
  }
  .title-band .accent { color: var(--green); margin-left: 5px; }
  .backdrop {
    position: absolute; right: 0; bottom: 20px; width: 62%; height: 55%;
    background: linear-gradient(160deg, rgba(255,255,255,0) 10%, var(--grey) 55%, var(--grey-mid));
    opacity: .8;
  }
  .columns {
    position: relative; display: grid; grid-template-columns: repeat(3, 1fr);
    gap: 8px; padding: 9px 14px 0;
  }
  .category { margin-bottom: 7px; }
  .category h2 {
    font-family: "Oswald", Arial, sans-serif; font-weight: 700; font-size: 8.5px;
    color: var(--purple); letter-spacing: .3px; margin-bottom: 2px;
    border-bottom: 1px solid var(--green); padding-bottom: 1px;
  }
  .category ul { list-style: none; font-size: 6.4px; line-height: 8px; }
  .footer {
    position: absolute; left: 0; right: 0; bottom: 0; height: 20px;
    background: linear-gradient(90deg, var(--green), var(--green-light));
    display: flex; align-items: center; justify-content: center;
    font-size: 6.5px; font-weight: 700; color: var(--purple-deep); letter-spacing: .4px;
  }
  .footer::before {
    content: ""; position: absolute; top: -4px; left: 0; right: 0; height: 4px; background: var(--purple);
  }
  .fleet-photo {
    width: 100%; height: 62px; margin: 2px 0 6px;
    background: linear-gradient(180deg, #9fb8d6, #5b6f8f 60%, #3a3550);
  }
  .contact h2 {
    font-family: "Oswald", Arial, sans-serif; font-weight: 700; font-size: 10px; color: var(--purple);
  }
  .contact-line { display: flex; align-items: center; gap: 3px; font-size: 6.4px; line-height: 9px; }
  .contact-line svg { width: 7px; height: 7px; fill: var(--green); }
</style>
</head>
<body>
<main class="canvas">

  <section class="page">
    <header>
      <div class="brand"><span class="brand-dot"></span><span class="brand-name">Tobin Chemical</span></div>
      <h1 class="title-band">CHEMICAL PRODUCT <span class="accent">LINE CARD</span></h1>
    </header>
    <div class="backdrop" role="img" aria-label="Faded photo of laboratory glassware"></div>
    <div class="columns">
      <div>
        <div class="category"><h2>SOLVENTS</h2><ul>
          <li>Acetone</li><li>Amyl Acetate</li><li>Aromatic 100</li><li>Aromatic 150</li><li>Butyl Acetate</li><li>Butyl Cellosolve</li><li>Cyclohexane</li><li>Dibasic Ester</li><li>Dimethyl Sulfoxide</li><li>Ethyl Acetate</li><li>Ethyl Lactate</li><li>Heptane</li><li>Hexane</li><li>Isoparaffin</li><li>Isopropyl Acetate</li><li>Kerosene</li><li>Lacquer Thinner</li><li>Limonene</li><li>Methyl Acetate</li><li>Methyl Ethyl Ketone</li><li>Methylene Chloride</li><li>Mineral Spirits</li><li>Odorless Spirits</li><li>Pentane</li><li>Propylene Carbonate</li><li>Tetrahydrofuran</li><li>Toluene</li><li>Xylene</li>
        </ul></div>
      </div>
      <div>
        <div class="category"><h2>ALCOHOLS</h2><ul>
          <li>Amyl Alcohol</li><li>Benzyl Alcohol</li><li>Cetyl Alcohol</li><li>Denatured Alcohol</li><li>Ethanol</li><li>Hexanol</li><li>Isobutanol</li><li>Isopropanol</li><li>Lauryl Alcohol</li><li>Methanol</li><li>n-Butanol</li><li>n-Propanol</li><li>Octanol</li><li>Stearyl Alcohol</li>
        </ul></div>
        <div class="category"><h2>GLYCOLS</h2><ul>
          <li>Butylene Glycol</li><li>Diethylene Glycol</li><li>Dipropylene Glycol</li><li>Ethylene Glycol</li><li>Glycerin</li><li>Hexylene Glycol</li><li>PEG 400</li><li>Propylene Glycol</li><li>Triethylene Glycol</li>
        </ul></div>
      </div>
      <div>
        <div class="category"><h2>OILS</h2><ul>
          <li>Castor Oil</li><li>Coconut Oil</li><li>Linseed Oil</li><li>Mineral Oil</li><li>Pine Oil</li><li>Silicone Oil</li><li>Soybean Oil</li><li>Tall Oil</li>
        </ul></div>
        <div class="category"><h2>METALS &amp; SALTS</h2><ul>
          <li>Aluminum Sulfate</li><li>Barium Sulfate</li><li>Calcium Chloride</li><li>Copper Sulfate</li><li>Ferric Chloride</li><li>Magnesium Sulfate</li><li>Manganese Sulfate</li><li>Nickel Sulfate</li><li>Potassium Chloride</li><li>Sodium Chloride</li><li>Zinc Oxide</li><li>Zinc Sulfate</li>
        </ul></div>
      </div>
    </div>
    <footer class="footer">www.tobinchemco.com</footer>
  </section>

  <section class="page">
    <header>
      <div class="brand"><span class="brand-dot"></span><span class="brand-name">Tobin Chemical</span></div>
      <h1 class="title-band">CHEMICAL PRODUCT <span class="accent">LINE CARD</span></h1>
    </header>
    <div class="backdrop" role="img" aria-label="Faded photo of laboratory glassware"></div>
    <div class="columns">
      <div>
        <div class="category"><h2>ACIDS</h2><ul>
          <li>Acetic Acid</li><li>Boric Acid</li><li>Citric Acid</li><li>Formic Acid</li><li>Glycolic Acid</li><li>Hydrochloric Acid</li><li>Lactic Acid</li><li>Nitric Acid</li><li>Oleic Acid</li><li>Oxalic Acid</li><li>Phosphoric Acid</li><li>Stearic Acid</li><li>Sulfamic Acid</li><li>Sulfuric Acid</li>
        </ul></div>
        <div class="category"><h2>SODIUM COMPOUNDS</h2><ul>
          <li>Sodium Bicarbonate</li><li>Sodium Bisulfite</li><li>Sodium Carbonate</li><li>Sodium Hydroxide</li><li>Sodium Hypochlorite</li><li>Sodium Metabisulfite</li><li>Sodium Nitrate</li><li>Sodium Silicate</li><li>Sodium Sulfate</li>
        </ul></div>
        <div class="category"><h2>AMINES</h2><ul>
          <li>Diethanolamine</li><li>Ethylenediamine</li><li>Monoethanolamine</li><li>Morpholine</li><li>Triethanolamine</li>
        </ul></div>
      </div>
      <div>
        <div class="category"><h2>SURFACTANTS</h2><ul>
          <li>Alcohol Ethoxylate</li><li>Betaine</li><li>Cocamide DEA</li><li>Nonylphenol Ethoxylate</li><li>Polysorbate 20</li><li>Polysorbate 80</li><li>Sodium Lauryl Sulfate</li>
        </ul></div>
        <div class="category"><h2>MISCELLANEOUS</h2><ul>
          <li>Activated Carbon</li><li>Ammonium Hydroxide</li><li>Bentonite Clay</li><li>Calcium Carbonate</li><li>Diatomaceous Earth</li><li>Hydrogen Peroxide</li><li>Kaolin</li><li>Talc</li><li>Titanium Dioxide</li><li>Urea</li>
        </ul></div>
      </div>
      <div>
        <div class="category"><h2>BY FUNCTION</h2><ul>
          <li>Chelating Agents</li><li>Corrosion Inhibitors</li><li>Defoamers</li><li>Dispersants</li><li>Emulsifiers</li><li>Preservatives</li><li>Thickeners</li><li>Wetting Agents</li>
        </ul></div>
        <div class="fleet-photo" role="img" aria-label="Photo of a company delivery truck"></div>
        <div class="contact">
          <h2>CALL US NOW</h2>
          <div class="contact-line">
            <svg viewBox="0 0 24 24" aria-hidden="true"><path d="M6.6 10.8a15.1 15.1 0 0 0 6.6 6.6l2.2-2.2a1 1 0 0 1 1-.25 11.4 11.4 0 0 0 3.6.57 1 1 0 0 1 1 1V20a1 1 0 0 1-1 1A17 17 0 0 1 3 4a1 1 0 0 1 1-1h3.5a1 1 0 0 1 1 1c0 1.25.2 2.45.57 3.57a1 1 0 0 1-.25 1z"/></svg>
            <span>(555) 014-2290</span>
          </div>
          <div class="contact-line">
            <svg viewBox="0 0 24 24" aria-hidden="true"><path d="M12 2a7 7 0 0 0-7 7c0 5.25 7 13 7 13s7-7.75 7-13a7 7 0 0 0-7-7zm0 9.5A2.5 2.5 0 1 1 12 6.5a2.5 2.5 0 0 1 0 5z"/></svg>
            <span>Ships nationwide daily</span>
          </div>
        </div>
      </div>
    </div>
    <footer class="footer">www.tobinchemco.com</footer>
  </section>

</main>
</body>
</html>
```